A5 Certificate for a running Bluecrest Challenge

I would like a certificate designed called the "Bluecrest 50K Running Challenge"

It is presented to people that have run 50k in Mallorca across 10 runs. So they have to run 10 runs with a minimum distance of 5K per run. This gives a total of 50k.

The certificate will need:

1. Map of Mallorca in the background
2. Picture of a runner
3. Main title at the front to say "Bluecrest 50k Running Challenge"
4. Space to put the runners name on it. "Awarded to:"
5. Space to put the date the certificate is awarded. "Date Awarded:"

The design is then up to you but it needs to look official and professional. It is designed for teenagers so it needs to be "cool" and bold.

Any questions please ask.

Target Market(s)

Teenagers who want something cool and bold.

Font styles to use
Sans Serif

Colors
0556a4
fbee3f
33a6d7

Requirements
Must have
• 1. Map of Mallorca in the background
• 2. Picture of a runner
• 3. Main title at the front to say "Bluecrest 50k Running Challenge"
• 4. Space to put the runners name on it. "Awarded to:"
• 5. Space to put the date the certificate is awarded. "Date Awarded:"
Nice to have
• Mallorca is a sunny holiday location so it would be good to have sea blue colours and the sun in the design. to show the running challenge was done on a holiday island.

```html
<!DOCTYPE html>
<html lang="en">
<head>
<meta charset="utf-8">
<title>Bluecrest 50k Running Challenge Certificate</title>
<link href="https://fonts.googleapis.com/css2?family=Noto+Serif:ital,wght@0,700;1,400;1,700&family=Montserrat:wght@800&display=swap" rel="stylesheet">
<style>
  :root {
    --paper: #eef3f5;
    --blue-deep: #0556a4;
    --blue-mid: #1b74c9;
    --blue-sky: #33a6d7;
    --blue-pale: #b9dcf0;
    --gold: #d9b13a;
    --gold-light: #f5dc78;
    --ink: #1a1a1a;
    --map-tone: #dfe8ec;
    --runner-tone: #aab4d6;
  }
  html, body {
    margin: 0;
    padding: 0;
    width: 1200px;
    height: 849px;
    overflow: hidden;
    background: var(--paper);
  }
  .certificate {
    position: relative;
    width: 1200px;
    height: 849px;
    overflow: hidden;
    background: var(--paper);
    font-family: "Noto Serif", Georgia, serif;
  }
  .corner-bands {
    position: absolute;
    inset: 0;
  }
  .island-map {
    position: absolute;
    left: 190px;
    top: 30px;
    width: 920px;
    height: 780px;
    border-radius: 46% 40% 44% 38%;
    background: radial-gradient(ellipse at 55% 45%, var(--map-tone) 0%, rgba(223,232,236,0.6) 60%, rgba(223,232,236,0) 80%);
  }
  .runner-figures {
    position: absolute;
    left: 195px;
    top: 190px;
    width: 720px;
    height: 580px;
    border-radius: 40%;
    background: radial-gradient(ellipse at 50% 50%, rgba(170,180,214,0.45) 0%, rgba(170,180,214,0.2) 55%, rgba(170,180,214,0) 75%);
  }
  .frame {
    position: absolute;
    inset: 0;
  }
  .award-seal {
    position: absolute;
    left: 100px;
    top: 70px;
    width: 220px;
    height: 290px;
  }
  .seal-label {
    position: absolute;
    left: 0;
    top: 78px;
    width: 220px;
    text-align: center;
    font-family: "Montserrat", Arial, sans-serif;
    font-weight: 800;
    color: var(--gold-light);
    line-height: 1;
  }
  .seal-year { font-size: 34px; letter-spacing: 1px; }
  .seal-word { font-size: 19px; margin-top: 6px; letter-spacing: 1px; }
  .title {
    position: absolute;
    left: 0;
    width: 1200px;
    text-align: center;
    margin: 0;
    background: linear-gradient(180deg, var(--blue-sky) 0%, var(--blue-mid) 45%, var(--blue-deep) 100%);
    -webkit-background-clip: text;
    background-clip: text;
    color: transparent;
  }
  .title-main {
    top: 242px;
    font-size: 82px;
    font-weight: 700;
    letter-spacing: 2px;
  }
  .title-sub {
    top: 352px;
    font-size: 74px;
    font-style: italic;
    font-weight: 700;
  }
  .field-label {
    position: absolute;
    left: 0;
    width: 1200px;
    text-align: center;
    font-style: italic;
    font-weight: 400;
    font-size: 40px;
    color: var(--ink);
  }
  .awarded-label { top: 503px; }
  .date-label { top: 628px; }
  .field-line {
    position: absolute;
    left: 408px;
    width: 387px;
    height: 2px;
    background: var(--ink);
  }
  .awarded-line { top: 586px; }
  .date-line { top: 714px; }
</style>
</head>
<body>
<main class="certificate">
  <div class="island-map" role="img" aria-label="Faint illustrated map of the island in the background"></div>

  <svg class="corner-bands" width="1200" height="849" viewBox="0 0 1200 849" aria-hidden="true">
    <polygon points="0,0 460,0 0,470" fill="var(--blue-sky)"/>
    <polygon points="140,0 420,0 0,430 0,160" fill="var(--blue-mid)"/>
    <polygon points="250,0 395,0 0,405 0,260" fill="var(--blue-deep)"/>
    <polygon points="420,0 470,0 0,480 0,432" fill="#ffffff"/>
    <polygon points="1200,400 1200,849 760,849" fill="var(--blue-pale)"/>
    <polygon points="1200,440 1200,849 800,849" fill="var(--blue-sky)"/>
    <polygon points="1200,520 1200,849 880,849" fill="var(--blue-mid)"/>
    <polygon points="1200,610 1200,849 970,849" fill="var(--blue-deep)"/>
  </svg>

  <div class="runner-figures" role="img" aria-label="Faint silhouettes of two runners mid-stride"></div>

  <svg class="frame" width="1200" height="849" viewBox="0 0 1200 849" aria-hidden="true">
    <rect x="31" y="31" width="1138" height="787" fill="none" stroke="var(--gold)" stroke-width="3"/>
    <rect x="40" y="40" width="1120" height="769" fill="none" stroke="var(--gold)" stroke-width="1.5"/>
  </svg>

  <div class="award-seal">
    <svg width="220" height="290" viewBox="0 0 220 290" aria-hidden="true">
      <polygon points="52,150 168,150 168,285 110,245 52,285" fill="var(--blue-deep)"/>
      <circle cx="110" cy="109" r="105" fill="var(--gold)"/>
      <circle cx="110" cy="109" r="98" fill="var(--gold-light)"/>
      <circle cx="110" cy="109" r="92" fill="var(--blue-deep)"/>
      <circle cx="110" cy="109" r="86" fill="none" stroke="var(--gold)" stroke-width="1.5"/>
      <circle cx="110" cy="168" r="4" fill="var(--gold-light)"/>
    </svg>
    <div class="seal-label">
      <div class="seal-year">2019</div>
      <div class="seal-word">AWARD</div>
    </div>
  </div>

  <h1 class="title title-main">BLUECREST</h1>
  <h2 class="title title-sub">50k Running Challenge</h2>

  <p class="field-label awarded-label" style="margin:0">Awarded to</p>
  <div class="field-line awarded-line"></div>
  <p class="field-label date-label" style="margin:0">Date Awarded</p>
  <div class="field-line date-line"></div>
</main>
</body>
</html>
```